Business cards and Stationary | Corvel Music Events

Hello! We need business cards and stationery for a new small business in the music industry. "Corvel is a high-end music agency which provides an unparalleled level of talent and personalized service to the realm entertainment, corporate events, and luxury weddings. Here is where the classical meets the contemporary and we can bring your vision to life.Keeping a steady finger on the pulse of current trends and consistently raising the bar for industry standards, Corvel continues to rise to the forefront of the music industry, providing the utmost professional, high-end, elegant, and engaging entertainment in Australia and World-Wide."

Target Market(s)

Class A. high profile corporate business.

Industry/Entity Type

Entertainment

Contact Information for Business Card

Corvel Music Events

Tessa Holloway
Director | Violinist

Level 7, 41 Marlow Street
Sydney, 2000

Website: www.corvelmusicevents.com
Phone number: 0481 352 604
Email: tessa@corvelmusicevents.com

Font styles to use
Serif
Sans Serif
Script

Colors
feeeee
0355a3
f59296
ffffff

Requirements
Nice to have
• Clean and sophisticated would be perfect.
• If there is a way to include the Instagram without being tacky, that would be awesome
• @corvelmusicevents
• Our website and logo have the following fonts:
• The primary logo is inspired and based on a font called BillionScript but the B is completely hand drawn and the rest is customised a bit to work together cohesively
• Monserrat Light - Is the Music part of the logo and as headers in the site
• Open Sans 300 and 400 (Light or Regular) is used mostly as the body text in the site
• If you want to access the website:
• www.corvelmusicevents.com
• username: client
• password: preview

```html
<!DOCTYPE html>
<html lang="en">
<head>
<meta charset="utf-8">
<title>Corvel Music Events – Business Card</title>
<link rel="stylesheet" href="https://fonts.googleapis.com/css2?family=Open+Sans:wght@300;400;600&display=swap">
<style>
  :root {
    --backdrop: #ddd3c8;
    --paper: #ffffff;
    --ink-brown: #a0573b;
    --ink-soft: #b27a62;
    --logo-light: #f3d3cc;
    --wood-dark: #2a1810;
    --wood-mid: #6b3a1e;
    --wood-warm: #b86a2c;
    --wood-gold: #d99a45;
  }
  * { margin: 0; padding: 0; box-sizing: border-box; }
  html, body { width: 1200px; height: 800px; overflow: hidden; }
  body {
    background: var(--backdrop);
    font-family: "Open Sans", Arial, sans-serif;
    position: relative;
  }
  .card {
    position: absolute;
    top: 248px;
    width: 525px;
    height: 300px;
    overflow: hidden;
    box-shadow: 0 6px 18px rgba(60, 40, 25, 0.18);
  }
  .card--front { left: 50px; }
  .card--back { left: 625px; background: var(--paper); }

  .photo-fill {
    position: absolute;
    inset: 0;
    background:
      radial-gradient(ellipse at 75% 40%, var(--wood-gold) 0%, var(--wood-warm) 22%, transparent 50%),
      linear-gradient(160deg, var(--wood-dark) 0%, #3e2416 35%, var(--wood-mid) 60%, #4a2a18 100%);
  }

  .wordmark {
    position: absolute;
    font-weight: 300;
    letter-spacing: 0.04em;
    white-space: nowrap;
    line-height: 1;
  }
  .card--front .wordmark {
    left: 40px;
    bottom: 56px;
    font-size: 44px;
    color: var(--logo-light);
  }
  .card--back .wordmark {
    left: 34px;
    top: 134px;
    font-size: 29px;
    color: var(--ink-brown);
  }

  .contact {
    position: absolute;
    left: 272px;
    top: 76px;
    width: 228px;
    color: var(--ink-soft);
  }
  .contact__name {
    font-size: 16px;
    font-weight: 600;
    color: var(--ink-brown);
    line-height: 1.2;
  }
  .contact__role {
    font-size: 9.5px;
    margin-bottom: 7px;
  }
  .contact__list { list-style: none; }
  .contact__item {
    display: flex;
    align-items: center;
    gap: 5px;
    font-size: 9.5px;
    line-height: 1.8;
    white-space: nowrap;
  }
  .contact__icon { width: 9px; height: 9px; flex: none; }
  .contact__sep { margin-left: 6px; }

  .photo-inset { position: absolute; }
  .photo-inset--bottom { left: 215px; bottom: 0; width: 310px; height: 84px; }
  .photo-inset--top { right: 0; top: 0; width: 200px; height: 60px; }
</style>
</head>
<body>

<section class="card card--front" aria-label="Business card front">
  <div class="photo-fill" role="img" aria-label="Close-up photograph of a violin scroll and fingerboard"></div>
  <div class="wordmark">Corvel Music</div>
</section>

<section class="card card--back" aria-label="Business card back">
  <svg class="photo-inset photo-inset--top" viewBox="0 0 200 60" role="img" aria-label="Small photograph of a violin">
    <defs>
      <linearGradient id="insetTop" x1="0" y1="0" x2="1" y2="1">
        <stop offset="0" stop-color="#e9ddd2"/>
        <stop offset="0.6" stop-color="#a45a2a"/>
        <stop offset="1" stop-color="#5a2e16"/>
      </linearGradient>
    </defs>
    <polygon points="40,0 200,0 200,48 70,48" fill="url(#insetTop)"/>
    <polyline points="30,0 62,54 200,54" fill="none" stroke="#c9a590" stroke-width="1"/>
    <polyline points="22,0 56,60 200,60" fill="none" stroke="#c9a590" stroke-width="1"/>
  </svg>

  <div class="wordmark">Corvel Music</div>

  <div class="contact">
    <p class="contact__name">Example Name</p>
    <p class="contact__role">Designation</p>
    <ul class="contact__list">
      <li class="contact__item">
        <svg class="contact__icon" viewBox="0 0 10 10"><circle cx="5" cy="5" r="5" fill="var(--ink-brown)"/><path d="M5 2.2a1.8 1.8 0 0 1 1.8 1.8C6.8 5.4 5 7.8 5 7.8S3.2 5.4 3.2 4A1.8 1.8 0 0 1 5 2.2z" fill="#fff"/></svg>
        Level 7, 41 Marlow Street, Sydney, 2000
      </li>
      <li class="contact__item">
        <svg class="contact__icon" viewBox="0 0 10 10"><circle cx="5" cy="5" r="5" fill="var(--ink-brown)"/><rect x="3.4" y="2.2" width="3.2" height="5.6" rx="0.6" fill="#fff"/></svg>
        0481 352 604
        <svg class="contact__icon contact__sep" viewBox="0 0 10 10"><circle cx="5" cy="5" r="5" fill="var(--ink-brown)"/><path d="M3.2 2.6l1 1-0.6 0.8 1.8 1.8 0.8-0.6 1 1-0.8 1C4.8 7.4 2.6 5.2 2.4 3.4z" fill="#fff"/></svg>
        0481 352 604
      </li>
      <li class="contact__item">
        <svg class="contact__icon" viewBox="0 0 10 10"><circle cx="5" cy="5" r="5" fill="var(--ink-brown)"/><rect x="2.4" y="3.2" width="5.2" height="3.6" fill="#fff"/><path d="M2.4 3.2L5 5.2 7.6 3.2" fill="none" stroke="var(--ink-brown)" stroke-width="0.6"/></svg>
        contact@corvelmusicevents.com
      </li>
      <li class="contact__item">
        <svg class="contact__icon" viewBox="0 0 10 10"><circle cx="5" cy="5" r="5" fill="var(--ink-brown)"/><circle cx="5" cy="5" r="2.6" fill="none" stroke="#fff" stroke-width="0.7"/><path d="M2.4 5h5.2M5 2.4v5.2" stroke="#fff" stroke-width="0.6"/></svg>
        www.corvelmusicevents.com
      </li>
    </ul>
  </div>

  <svg class="photo-inset photo-inset--bottom" viewBox="0 0 310 84" role="img" aria-label="Small photograph of a violin scroll and pegs">
    <defs>
      <linearGradient id="insetBottom" x1="0" y1="0" x2="1" y2="0">
        <stop offset="0" stop-color="#e6dbd0"/>
        <stop offset="0.45" stop-color="#b36430"/>
        <stop offset="1" stop-color="#7a3c1c"/>
      </linearGradient>
    </defs>
    <polygon points="40,84 68,20 310,20 310,84" fill="url(#insetBottom)"/>
    <polyline points="28,84 61,12 310,12" fill="none" stroke="#c9a590" stroke-width="1"/>
    <polyline points="18,84 55,4 310,4" fill="none" stroke="#c9a590" stroke-width="1"/>
  </svg>
</section>

</body>
</html>
```